KWT Contracting services . Building and maintenance services, optic fibre installation

Business cards and logo design.I need a logo that I can use on business cards ,workwear and on my vehicles. I would like the KWT to be the main or larger text and contracting services to be the smaller or less important text.I like monograms, modern designs and repeating patterns symbols. I am also a Gemini and my favourite number is 22 so if this can be any inspiration to help with the design. Am thinking of the using German flag colours as a his is my family’s heritage. And the other 2 main colours I wear is black and white.But any ideas are appreciated.I do not need a design that is trade specific but a design that could be used for any business.

Target Market(s)

General public

Contact Information for Business Card

KWT Contracting Services ( front of business card)

(Back of business card)
Milo Brackwood
0471539264
Maintenance services
Optic fibre and data installation

Logo Text

Logo can just be pattern or monogram or incorporate KWT . I like the gemini star sign and the number 22

Colors
ec1f27
000000
fbee3e
ffffff

Requirements
Must have
• Logo and KWT Contracting Services on the front of business card
Nice to have
• Possible use of German flag colours.
• Modern design.
• Design to be able to be used on black or white background as I want to put it on clothing

```html
<!DOCTYPE html>
<html lang="en">
<head>
<meta charset="utf-8">
<title>KWT Contracting Services – Business Cards</title>
<link rel="stylesheet" href="https://fonts.googleapis.com/css2?family=Open+Sans:wght@400;600;700&display=swap">
<style>
  :root {
    --stage: #262626;
    --card: #111111;
    --card-edge: #1a1a1a;
    --brand-red: #ec1f27;
    --brand-yellow: #fbee3e;
    --ink-white: #ffffff;
    --rule-grey: #8a8a8a;
  }
  * { box-sizing: border-box; margin: 0; padding: 0; }
  html, body {
    width: 1200px;
    height: 900px;
    overflow: hidden;
    background: var(--stage);
    font-family: "Open Sans", Arial, sans-serif;
  }
  .stage {
    width: 1200px;
    height: 900px;
    display: flex;
    flex-direction: column;
    align-items: center;
    justify-content: center;
    gap: 48px;
  }
  .card {
    position: relative;
    width: 560px;
    height: 320px;
    background: linear-gradient(160deg, var(--card-edge), var(--card));
    overflow: hidden;
    box-shadow: 0 14px 30px rgba(0,0,0,0.45);
  }
  .card__band {
    position: absolute;
    left: 0; right: 0; bottom: 0;
    height: 10px;
    background: var(--brand-red);
  }
  /* Front */
  .card--front {
    display: flex;
    align-items: center;
    justify-content: center;
  }
  .brand {
    display: flex;
    align-items: center;
    gap: 22px;
    margin-top: -16px;
  }
  .brand__dot {
    width: 64px;
    height: 64px;
    border-radius: 50%;
    background: var(--brand-red);
  }
  .brand__name {
    color: var(--ink-white);
    font-weight: 700;
    line-height: 1;
  }
  .brand__initials {
    display: block;
    font-size: 72px;
    letter-spacing: 10px;
  }
  .brand__descriptor {
    display: block;
    font-size: 14px;
    letter-spacing: 0.5px;
    margin-top: 4px;
    text-transform: uppercase;
  }
  /* Back */
  .card--back {
    display: flex;
    flex-direction: column;
    align-items: center;
    justify-content: center;
    text-align: center;
    padding-bottom: 10px;
  }
  .contact__name {
    color: var(--brand-red);
    font-weight: 700;
    font-size: 20px;
    text-transform: uppercase;
    letter-spacing: 0.3px;
  }
  .contact__phone {
    color: var(--ink-white);
    font-weight: 400;
    font-size: 22px;
    letter-spacing: 1px;
    margin-top: 4px;
  }
  .contact__rule {
    width: 170px;
    height: 1px;
    background: var(--rule-grey);
    margin: 8px 0 12px;
  }
  .services {
    list-style: none;
    color: var(--ink-white);
    font-size: 16px;
    line-height: 1.25;
    text-transform: uppercase;
  }
</style>
</head>
<body>
  <main class="stage">
    <section class="card card--front" aria-label="Business card front">
      <div class="brand">
        <span class="brand__dot" aria-hidden="true"></span>
        <h1 class="brand__name">
          <span class="brand__initials">KWT</span>
          <span class="brand__descriptor">Contracting Services</span>
        </h1>
      </div>
      <div class="card__band"></div>
    </section>

    <section class="card card--back" aria-label="Business card back">
      <h2 class="contact__name">Milo Brackwood</h2>
      <p class="contact__phone">0471539264</p>
      <div class="contact__rule"></div>
      <ul class="services">
        <li>Maintenance Services</li>
        <li>Optic Fibre and Data Installation</li>
      </ul>
      <div class="card__band"></div>
    </section>
  </main>
</body>
</html>
```